Letter Head, for use on daily correspondence with other companies

Hi

I want a professional Letter head, That my company can use to corresponded with other companies we do business with on a daily basis.

I want this done as soon as possible as this is peak session for us.

I have attached the company logo so please be creative and professional.
Kind regards

Marcus

Target Market(s)

All Audience searching for tickets, people in the entertainment world

Industry/Entity Type

Entertainment Industry

Font styles to use
Serif
Sans Serif
Decorative
Script

Requirements
Must have
• Very professional image.
• I will know want i want when i see it
• so please do your utmost in your professional standards
• Address of the company 24 hollin lane, telephone number 0207 562 3198
• Vat number: 487 2915 06.
• This letter head my be able to acomodate usage for directors & CEO as well as managers and employess
Nice to have
• A great professional image
Should not have
• Be creative please

```html
<!DOCTYPE html>
<html lang="en">
<head>
<meta charset="utf-8">
<title>Stagepass Letterhead</title>
<link rel="stylesheet" href="https://fonts.googleapis.com/css2?family=Noto+Sans:wght@400;700&display=swap">
<style>
  :root {
    --paper: #ffffff;
    --band-grey: #717171;
    --bar-dark: #333333;
    --bar-red: #cc2200;
    --label-red: #e8452a;
    --text-light: #ffffff;
    --brand-ink: #111111;
  }
  * { margin: 0; padding: 0; box-sizing: border-box; }
  html, body {
    width: 927px;
    height: 1200px;
    overflow: hidden;
    background: var(--paper);
  }
  .letterhead {
    position: relative;
    width: 927px;
    height: 1200px;
    background: var(--paper);
    font-family: "Noto Sans", Verdana, sans-serif;
  }
  .header-art {
    position: absolute;
    top: 0;
    left: 0;
    display: block;
  }
  .brand-name {
    position: absolute;
    left: 25px;
    top: 70px;
    font-size: 36px;
    font-weight: 700;
    letter-spacing: -0.5px;
    color: var(--brand-ink);
    line-height: 1;
  }
  .company-contact {
    position: absolute;
    left: 671px;
    top: 43px;
    font-size: 11px;
    line-height: 16.4px;
    color: var(--text-light);
    font-style: normal;
  }
  .company-contact .contact-label {
    font-weight: 700;
    color: var(--label-red);
  }
</style>
</head>
<body>
  <main class="letterhead">
    <svg class="header-art" width="927" height="140" viewBox="0 0 927 140" aria-hidden="true">
      <rect class="bar-dark" x="15" y="16" width="239" height="14" fill="var(--bar-dark)"/>
      <rect class="bar-red" x="254" y="16" width="659" height="14" fill="var(--bar-red)"/>
      <rect class="band-grey" x="15" y="30" width="898" height="106" fill="var(--band-grey)"/>
      <path class="brand-cutout" d="M15,137 L15,54 L160,54 C205,54 222,78 235,106 C247,130 257,136 272,136 L272,137 Z" fill="var(--paper)"/>
    </svg>

    <div class="brand-name">Stagepass</div>

    <address class="company-contact">
      <div class="contact-label">Company Address:</div>
      <div class="contact-line">24 Hollin Lane</div>
      <div class="contact-line">Phone: 0207 562 3198</div>
      <div class="contact-line">Fax: 565- 318- 2409</div>
    </address>
  </main>
</body>
</html>
```